Two sided business card template for:

Room 4 Keeps Storage
1817 Brantley Avenue,
Saskatoon, SK
R3P 2W6
306-555-0184
www.room4keeps.ca

Front side should be standard business card information. Sample should be for Gregory Lindell, Operations Manager, greg@room4keeps.ca

Back side should be an advertisement for the storage facility. Some points about our facility are below you may use some or all of these features in the ad.

-Online payments and bookings
-Seasonal bicycle, tire, and motorcycle storage
-24hr self storage access
-Safe, and secure, with digital video surveillance
-Airport location

Card could have, but doesn't need a clever tag line containing the company name

Finished design must be in Microsoft word, or publisher format, and text must be editable.

```html
<!DOCTYPE html>
<html lang="en">
<head>
<meta charset="utf-8">
<title>Room 4 Keeps Storage – Business Card</title>
<link rel="stylesheet" href="https://fonts.googleapis.com/css2?family=Exo+2:wght@400;600;700&display=swap">
<style>
  :root {
    --page: #e8e5e1;
    --card-white: #ffffff;
    --charcoal: #3c3c3d;
    --charcoal-deep: #232324;
    --brand-red: #d5333a;
    --ink: #1d1d1d;
    --light-text: #f2f2f2;
    --muted-text: #d6d6d6;
  }
  * { margin: 0; padding: 0; box-sizing: border-box; }
  html, body { width: 1200px; height: 914px; overflow: hidden; }
  body {
    background: var(--page);
    font-family: "Exo 2", "Segoe UI", sans-serif;
    position: relative;
  }
  .card {
    position: absolute;
    left: 240px;
    width: 720px;
    height: 411px;
    background: var(--card-white);
    box-shadow: 0 8px 24px rgba(0,0,0,.18);
    overflow: hidden;
  }
  .card--back { top: 31px; }
  .card--front { top: 472px; }
  .card__shapes { position: absolute; inset: 0; width: 100%; height: 100%; }

  .brand {
    position: absolute;
    display: flex;
    align-items: center;
    gap: 14px;
  }
  .brand__mark {
    width: 46px; height: 46px;
    background: var(--brand-red);
    flex: none;
  }
  .brand__name {
    font-weight: 700;
    font-size: 30px;
    line-height: 1.02;
    color: var(--ink);
    text-transform: uppercase;
    letter-spacing: .5px;
  }
  .card--front .brand { left: 70px; top: 62px; }
  .card--back .brand { left: 468px; top: 168px; }

  .features {
    position: absolute;
    left: 52px; top: 62px;
    list-style: none;
    color: var(--light-text);
    font-size: 15px;
    line-height: 1.45;
  }

  .contact {
    position: absolute;
    right: 46px; bottom: 34px;
    text-align: right;
    color: var(--light-text);
  }
  .contact__name { font-size: 23px; font-weight: 600; letter-spacing: .6px; }
  .contact__title { font-size: 14px; color: var(--muted-text); margin-bottom: 22px; }
  .contact__line {
    display: flex; justify-content: flex-end; align-items: center;
    gap: 12px; font-size: 15px; line-height: 1.55;
  }
  .contact__icon { width: 16px; height: 16px; fill: var(--light-text); flex: none; }
  .contact__address { font-size: 15px; line-height: 1.55; margin-right: 28px; }
</style>
</head>
<body>

<section class="card card--back" aria-label="Card back">
  <svg class="card__shapes" viewBox="0 0 720 411" preserveAspectRatio="none" aria-hidden="true">
    <path d="M0 0 L480 0 C548 130 520 300 350 411 L0 411 Z" fill="var(--brand-red)"/>
    <path d="M0 0 L456 0 C524 130 496 300 326 411 L0 411 Z" fill="var(--charcoal)"/>
  </svg>
  <ul class="features">
    <li>Online payments and bookings</li>
    <li>Seasonal bicycle, tire, and motorcycle storage</li>
    <li>24hr self storage access</li>
    <li>Safe, and secure, with digital video surveillance</li>
    <li>Airport location</li>
  </ul>
  <div class="brand">
    <span class="brand__mark"></span>
    <span class="brand__name">Room 4 Keeps<br>Storage</span>
  </div>
</section>

<section class="card card--front" aria-label="Card front">
  <svg class="card__shapes" viewBox="0 0 720 411" preserveAspectRatio="none" aria-hidden="true">
    <path d="M398 0 C462 170 380 330 150 411 L720 411 L720 0 Z" fill="var(--brand-red)"/>
    <path d="M426 0 C488 170 410 335 184 411 L720 411 L720 0 Z" fill="var(--charcoal-deep)"/>
    <path d="M434 0 C496 172 420 338 198 411 L720 411 L720 0 Z" fill="var(--charcoal)"/>
  </svg>
  <div class="brand">
    <span class="brand__mark"></span>
    <span class="brand__name">Room 4 Keeps<br>Storage</span>
  </div>
  <div class="contact">
    <p class="contact__name">Gregory Lindell</p>
    <p class="contact__title">Operations Manager</p>
    <p class="contact__line">306-555-0184
      <svg class="contact__icon" viewBox="0 0 16 16" aria-hidden="true"><circle cx="8" cy="5" r="3.5"/><path d="M1.5 16 C1.5 10.5 14.5 10.5 14.5 16 Z"/></svg>
    </p>
    <p class="contact__line">www.room4keeps.ca
      <svg class="contact__icon" viewBox="0 0 16 16" aria-hidden="true"><circle cx="8" cy="8" r="7" fill="none" stroke="var(--light-text)" stroke-width="1.6"/><path d="M1 8 H15 M8 1 C4 5 4 11 8 15 M8 1 C12 5 12 11 8 15" fill="none" stroke="var(--light-text)" stroke-width="1.2"/></svg>
    </p>
    <p class="contact__line">greg@room4keeps.ca
      <svg class="contact__icon" viewBox="0 0 16 16" aria-hidden="true"><rect x="1" y="3" width="14" height="10" fill="none" stroke="var(--light-text)" stroke-width="1.6"/><path d="M1 3 L8 9 L15 3" fill="none" stroke="var(--light-text)" stroke-width="1.6"/></svg>
    </p>
    <p class="contact__address">1817 Brantley Avenue, Saskatoon, SK R3P 2W6</p>
  </div>
</section>

</body>
</html>
```